Personal Blog

The wordpress blog style and layout should be similar to http://www.danholtmere.com

homepage: my photo, list of things, call to action then 3 boxes (The Blog, The Book and podcast)

Other pages: About us, Blog, Consulting, Contact

Target Market(s)

Web Marketing Consultant

Industry/Entity Type

Consulting

Colors
3277b5
33a6d7
f04a50
f68e4e
33b7a4

```html
<!DOCTYPE html>
<html lang="en">
<head>
<meta charset="utf-8">
<title>Karim Althessa – Web Marketing Consultant</title>
<link href="https://fonts.googleapis.com/css2?family=Arimo:ital,wght@0,400;0,700;1,400;1,700&family=Raleway:wght@500;600;700&family=Archivo+Narrow:wght@700&display=swap" rel="stylesheet">
<style>
  :root{
    --orange:#dc6422;
    --orange-bright:#f68e4e;
    --ink:#1b1b1b;
    --header:#1c1c1c;
    --footer:#202020;
    --base:#121212;
    --text:#222;
    --muted:#666;
    --light:#f0f0f0;
    --white:#fff;
  }
  *{box-sizing:border-box;margin:0;padding:0}
  html,body{width:742px;height:1200px;overflow:hidden;background:var(--white)}
  body{font-family:Arimo,Arial,sans-serif;color:var(--text);position:relative}
  .page{position:relative;width:742px;height:1200px;overflow:hidden}
  .abs{position:absolute}

  /* header */
  .site-header{position:absolute;left:0;top:0;width:742px;height:72px;background:var(--header)}
  .brand{position:absolute;left:65px;top:25px;display:flex;align-items:center;gap:9px;
    font-family:Raleway,Arial,sans-serif;font-weight:700;font-size:21px;color:var(--white);letter-spacing:.2px}
  .brand-mark{width:18px;height:18px;background:var(--orange);border-radius:3px}
  .main-nav a{position:absolute;top:33px;font-size:10px;color:var(--white);text-decoration:none;line-height:10px}
  .main-nav a.is-active{top:31px;left:321px;width:53px;height:20px;line-height:20px;text-align:center;
    background:#444;color:var(--orange-bright);border:1px solid #555;border-radius:2px;top:31px}

  /* hero */
  .hero{position:absolute;left:0;top:72px;width:742px;height:270px;
    background:linear-gradient(100deg,#3a2a22 0%,#4b4644 30%,#5d6b75 55%,#3e4c57 80%,#2d3742 100%)}
  .hero-portrait{position:absolute;left:305px;top:40px;width:378px;height:230px;
    background:radial-gradient(ellipse at 70% 55%,#c9d3e0 0%,#9aa6b4 45%,rgba(80,90,100,0) 75%)}
  .hero-title{position:absolute;left:63px;top:46px;color:var(--white);font-size:14px;line-height:25px}
  .hero-title strong{color:var(--orange-bright);font-size:16px;font-weight:700}
  .topic-list{position:absolute;left:63px;top:116px;list-style:none}
  .topic-list li{display:flex;align-items:center;gap:6px;color:var(--white);font-size:10.5px;height:24.6px}
  .tick{width:9px;height:9px}

  .quote-badge{position:absolute;left:357px;top:327px;width:30px;height:30px;border-radius:50%;background:var(--orange);z-index:2}

  /* testimonial */
  .testimonial{position:absolute;left:0;top:342px;width:742px;height:86px;
    background:linear-gradient(90deg,#e4e4e4,#fafafa 50%,#e6e6e6)}
  .testimonial .mark{position:absolute;left:74px;top:20px;font-family:Georgia,serif;font-size:40px;color:#c8c8c8;line-height:40px}
  .testimonial blockquote{position:absolute;left:106px;top:28px;width:580px;font-style:italic;font-size:10.5px;line-height:17px;color:#555}
  .testimonial cite{position:absolute;right:87px;top:64px;font-size:9px;font-weight:700;color:var(--orange);font-style:italic}

  /* features */
  .features{position:absolute;left:0;top:428px;width:742px;height:275px;background:var(--orange)}
  .feature{position:absolute;top:24px;width:183px;height:226px;background:var(--white);
    border-top:3px solid var(--ink);border-bottom:3px solid var(--ink);text-align:center}
  .feature-icon{position:absolute;left:57px;top:16px;width:68px;height:68px;border-radius:50%;background:var(--orange)}
  .feature h2{position:absolute;left:0;width:100%;font-weight:400;font-size:19px;color:#111}
  .feature p{position:absolute;left:12px;width:159px;font-size:8px;line-height:12.5px;color:#222}
  .btn-outline{position:absolute;left:54px;width:74px;height:23px;border:1px solid #aaa;border-radius:2px;
    font-size:10px;color:var(--orange);line-height:21px}

  /* recent blogs */
  .recent{position:absolute;left:0;top:703px;width:742px;height:322px;background:var(--light)}
  .recent h2{position:absolute;left:0;top:24px;width:100%;text-align:center;font-family:Raleway,Arial,sans-serif;font-weight:500;font-size:17px;letter-spacing:.5px;color:#111}
  .post{position:absolute;top:68px;width:173px;height:222px;background:var(--white)}
  .post-thumb{width:173px;height:120px}
  .post h3{margin:7px 8px 0;font-family:"Archivo Narrow",Arial,sans-serif;font-size:10px;line-height:14px;letter-spacing:.3px;color:#111}
  .post p{margin:3px 8px 0;font-size:7.5px;line-height:11px;color:#555}
  .btn-solid{display:inline-block;margin:8px 8px 0;width:54px;height:17px;line-height:17px;text-align:center;
    background:var(--orange);color:var(--white);font-size:7.5px}

  /* footer */
  .site-footer{position:absolute;left:0;top:1025px;width:742px;height:147px;background:var(--footer)}
  .site-footer h4{position:absolute;top:22px;font-family:Raleway,Arial,sans-serif;font-weight:600;font-size:10px;color:var(--white)}
  .footer-about{position:absolute;left:87px;top:44px;width:172px;font-size:8px;line-height:11.8px;color:#5e5e5e}
  .field{position:absolute;left:287px;width:142px;height:18px;background:var(--white);font-size:7.5px;line-height:18px;padding-left:5px;color:#222}
  .join{position:absolute;left:287px;top:104px;width:142px;height:21px;background:var(--orange);
    font-family:Raleway,Arial,sans-serif;font-weight:700;color:var(--white);font-size:12px;line-height:21px;text-align:center}
  .contact-row{position:absolute;left:488px;width:180px;border-bottom:1px solid #2e2e2e;font-size:8.5px;line-height:12.5px;color:#6a6a6a}
  .contact-row svg{position:absolute;left:3px}
  .contact-row span{display:block;margin-left:20px}
  .contact-row .email{color:var(--orange-bright)}
  .copyright{position:absolute;left:0;top:1172px;width:742px;height:28px;background:var(--base);
    text-align:center;font-size:8.5px;line-height:28px;color:#6c6c6c}
</style>
</head>
<body>
<div class="page">

  <header class="site-header">
    <div class="brand"><span class="brand-mark"></span>Karim Althessa</div>
    <nav class="main-nav">
      <a class="is-active" href="#">ABOUT</a>
      <a href="#" style="left:393px">Blog</a>
      <a href="#" style="left:442px">Consulting</a>
      <a href="#" style="left:517px">Resources</a>
      <a href="#" style="left:592px">Book</a>
      <a href="#" style="left:642px">Contact</a>
    </nav>
  </header>

  <section class="hero" role="img" aria-label="Blurred office background">
    <div class="hero-portrait" role="img" aria-label="Portrait of the consultant smiling at a desk with a computer"></div>
    <p class="hero-title">Text ho here &amp; <strong>Product Management</strong><br>text here Online Marketing, to learn topics:</p>
    <ul class="topic-list">
      <li><svg class="tick" viewBox="0 0 10 10"><circle cx="5" cy="5" r="5" fill="#f68e4e"/><path d="M2.6 5.2l1.6 1.6 3.2-3.4" stroke="#fff" stroke-width="1.4" fill="none"/></svg>Product Management</li>
      <li><svg class="tick" viewBox="0 0 10 10"><circle cx="5" cy="5" r="5" fill="#f68e4e"/><path d="M2.6 5.2l1.6 1.6 3.2-3.4" stroke="#fff" stroke-width="1.4" fill="none"/></svg>Customer Development</li>
      <li><svg class="tick" viewBox="0 0 10 10"><circle cx="5" cy="5" r="5" fill="#f68e4e"/><path d="M2.6 5.2l1.6 1.6 3.2-3.4" stroke="#fff" stroke-width="1.4" fill="none"/></svg>Digital Marketing</li>
      <li><svg class="tick" viewBox="0 0 10 10"><circle cx="5" cy="5" r="5" fill="#f68e4e"/><path d="M2.6 5.2l1.6 1.6 3.2-3.4" stroke="#fff" stroke-width="1.4" fill="none"/></svg>Branding &amp; Reputation</li>
    </ul>
  </section>

  <svg class="quote-badge" viewBox="0 0 30 30"><circle cx="15" cy="15" r="15" fill="#dc6422"/><text x="15" y="25" text-anchor="middle" font-family="Georgia,serif" font-size="22" font-weight="700" fill="#fff">”</text></svg>

  <section class="testimonial">
    <span class="mark">“</span>
    <blockquote>"....I was blown away by his breadth of industry knowledge, the straight talking delivery and collaborative format. A highly recommended Social media experts and thought leader..."</blockquote>
    <cite>-Leon Marvette - Marketing</cite>
  </section>

  <section class="features">
    <article class="feature" style="left:63px">
      <svg class="feature-icon" viewBox="0 0 68 68"><circle cx="34" cy="34" r="34" fill="#dc6422"/>
        <path d="M18 25c0-5 5-8 11-8s11 3 11 8-5 8-11 8c-1.5 0-3 0-4-.5l-5 3 1.5-4C19 30 18 28 18 25z" fill="none" stroke="#fff" stroke-width="2.4"/>
        <path d="M42 29c5 1 8 4 8 7.5 0 2.5-1 4-3 5.5l1.5 4-5-3c-1 .5-2.5.5-4 .5-5 0-9-2.5-10-6" fill="none" stroke="#fff" stroke-width="2.4"/></svg>
      <h2 style="top:98px">The Blog</h2>
      <p style="top:132px">simply dummy text of the printing and type-setting industry. Lorem Ipsum has been the industry's standard dummy text ever since the 1500s</p>
      <div class="btn-outline" style="top:194px">Read More</div>
    </article>
    <article class="feature" style="left:279px">
      <svg class="feature-icon" viewBox="0 0 68 68"><circle cx="34" cy="34" r="34" fill="#dc6422"/>
        <path d="M22 47l6-27h20l-6 27z" fill="#fff"/><path d="M20 49l6-27" stroke="#fff" stroke-width="2.5"/>
        <path d="M31 26h13M30 30h13" stroke="#dc6422" stroke-width="1.5"/></svg>
      <h2 style="top:102px">The Book</h2>
      <p style="top:136px">simply dummy text of the printing and type-setting industry. Lorem Ipsum has been the industry's standard dummy text ever since the 1500s</p>
      <div class="btn-outline" style="top:198px">Read More</div>
    </article>
    <article class="feature" style="left:496px">
      <svg class="feature-icon" viewBox="0 0 68 68"><circle cx="34" cy="34" r="34" fill="#dc6422"/>
        <circle cx="29" cy="33" r="6.5" fill="#fff"/><path d="M17 50c1-7 6-10 12-10s11 3 12 10z" fill="#fff"/>
        <circle cx="43" cy="24" r="6" fill="none" stroke="#fff" stroke-width="1.6"/><path d="M43 22v5M43 20.5v.1" stroke="#fff" stroke-width="1.6"/></svg>
      <h2 style="top:102px">Consulting</h2>
      <p style="top:136px">simply dummy text of the printing and type-setting industry. Lorem Ipsum has been the industry's standard dummy text ever since the 1500s</p>
      <div class="btn-outline" style="top:198px">Read More</div>
    </article>
  </section>

  <section class="recent">
    <h2>RECENT BLOGS</h2>
    <article class="post" style="left:71px">
      <div class="post-thumb" role="img" aria-label="Laptop and coffee cup on a wooden table" style="background:linear-gradient(135deg,#2a2520,#6b5238 55%,#a07a4e)"></div>
      <h3>Yet Another video Post Format With Embedded Media</h3>
      <p>Ipsum is simply dummy text of the printing and typesetting industry. Lorem Ipsum has been the industry's standard</p>
      <span class="btn-solid">Watch Video</span>
    </article>
    <article class="post" style="left:287px">
      <div class="post-thumb" role="img" aria-label="Desk from above with keyboard, books and phone" style="background:linear-gradient(135deg,#d8c8b6,#c48a5e 55%,#9c6a44)"></div>
      <h3>Yet Another video Post Format With Embedded Media</h3>
      <p>Ipsum is simply dummy text of the printing and typesetting industry. Lorem Ipsum has been the industry's standard</p>
      <span class="btn-solid">Watch Video</span>
    </article>
    <article class="post" style="left:498px">
      <div class="post-thumb" role="img" aria-label="Person working on a laptop at a wooden table" style="background:linear-gradient(135deg,#3a3632,#6e5a45 50%,#2b3340)"></div>
      <h3>Yet Another video Post Format With Embedded Media</h3>
      <p>Ipsum is simply dummy text of the printing and typesetting industry. Lorem Ipsum has been the industry's standard</p>
      <span class="btn-solid">Watch Video</span>
    </article>
  </section>

  <footer class="site-footer">
    <h4 style="left:87px">About IT Consultants</h4>
    <p class="footer-about">Lorem Ipsum is simply dummy text of the printing and typesetting industry. Lorem Ipsum has been the industry's standard dummy text ever since the 1500s, when an unknown printer took a galley of type and scrambled it to make a type specimen book. It has survived not only five centuries,</p>

    <h4 style="left:284px">Join My New Business</h4>
    <div class="field" style="top:48px">Enter Your Name</div>
    <div class="field" style="top:78px">Enter Email Name</div>
    <div class="join">Join For Free!</div>

    <h4 style="left:488px">Contact Us</h4>
    <div class="contact-row" style="top:45px;height:48px">
      <svg width="10" height="10" viewBox="0 0 10 10" style="top:2px"><path d="M5 0v10M1 3h8M2 6h6" stroke="#6a6a6a" stroke-width="1.4"/></svg>
      <span>Northgate Studios, Inc.<br>4180 Willow Ridge Rd, Suite 210<br>Fairholm, IN 20419</span>
    </div>
    <div class="contact-row" style="top:97px;height:22px">
      <svg width="9" height="9" viewBox="0 0 10 10" style="top:2px"><path d="M2 0l2 2.5-1.2 1.5c.8 1.5 1.7 2.4 3.2 3.2L7.5 6 10 8 8.5 10C4 9.5.5 6 0 1.5z" fill="#6a6a6a"/></svg>
      <span>+(99) 555 210 4476</span>
    </div>
    <div class="contact-row" style="top:124px;height:20px;border-bottom:none">
      <svg width="10" height="8" viewBox="0 0 10 8" style="top:3px"><rect width="10" height="8" fill="#6a6a6a"/><path d="M0 0l5 4 5-4" stroke="#202020" stroke-width="1" fill="none"/></svg>
      <span class="email">hello@althessa-consult.com</span>
    </div>
  </footer>

  <div class="copyright">© 2014 Copyright - Karim Althessa . All rights reserved</div>
</div>
</body>
</html>
```